Environmental Plastics Infographic

We need a series of infographics that can be used individually or as a combined presentation. We'd like the combined piece to include an introduction and conclusion along with 4-5 infographics. Each infographic (information unit) should also work as a standalone. We are trying to help people visualize size proportions and ratios to put carbon footprint/life cycle data for EPS foam packaging in perspective. We are looking for something creative to help people understand what the figures represent in terms they are familiar with.
To view our typical company design/style please see our website at www.trellamark.org. Our primary RGB colors are: (187,140,9); (94,47,29); (94,138,164); and (164,167,15). Secondary RGB colors are (249,162,28) and (218,210,208). Our title/header font is DIN Next LT Pro and our copy font is Calibri 10.5 pt. We can deviate from the font specification if beneficial and welcome interesting text treatments and typography.
We want sufficient white space with easy to grasp message concept with visual components. The attachment showing data points present concepts on how to show the data impacts but are only representative of a baseline concept - we are confident a professional designer can do a much better job with better visual presentation.
Target Market(s)
The audience is international brand manufacturers (brightmoor, kavo), US legislators & government agencies.
Nice to have
- Other creative ideas on how to present this messaging is encouraged.

```html
<!DOCTYPE html>
<html lang="en">
<head>
<meta charset="utf-8">
<title>Life Cycle – 1 Ton of EPS</title>
<link rel="stylesheet" href="https://fonts.googleapis.com/css2?family=Barlow:wght@400;500;600;700&display=swap">
<style>
  :root {
    --band-blue: #86aad3;
    --brown: #5e2f1d;
    --orange: #f58f50;
    --lime: #acd136;
    --olive: #a4a70f;
    --light-blue: #86aad3;
    --white: #ffffff;
  }
  * { margin: 0; padding: 0; box-sizing: border-box; }
  html, body { width: 1200px; height: 857px; overflow: hidden; background: var(--white); }
  .infographic {
    position: relative; width: 1200px; height: 857px;
    font-family: "Barlow", sans-serif; color: var(--brown);
  }
  .header-band {
    position: absolute; left: 0; top: 0; width: 1200px; height: 206px;
    background: var(--band-blue);
  }
  .life-cycle {
    position: absolute; right: 867px; top: 35px;
    font-weight: 700; font-size: 76px; line-height: 62px;
    text-align: right; color: var(--brown); letter-spacing: 1px;
  }
  .headline {
    position: absolute; left: 390px; top: 55px;
    font-weight: 700; font-size: 98px; line-height: 1;
    color: var(--white); letter-spacing: 3px; white-space: nowrap;
  }
  .section-title {
    position: absolute; font-weight: 400; font-size: 39px; line-height: 1;
    white-space: nowrap; letter-spacing: 0.5px;
  }
  .figure {
    position: absolute; font-weight: 600; font-size: 89px; line-height: 1;
    color: var(--orange); letter-spacing: 3px;
  }
  .unit {
    position: absolute; font-weight: 600; font-size: 31px; line-height: 1;
    letter-spacing: 1px; white-space: nowrap;
  }
  .note {
    position: absolute; font-weight: 600; font-size: 22px; line-height: 30px;
    white-space: nowrap;
  }
  .icon { position: absolute; }
</style>
</head>
<body>
<main class="infographic">
  <header class="header-band">
    <div class="life-cycle">LIFE<br>CYCLE</div>
    <h1 class="headline">1 TON OF EPS =</h1>
  </header>

  <!-- Global warming -->
  <h2 class="section-title" style="left:114px; top:278px;">Global Warming</h2>
  <svg class="icon car-icon" style="left:114px; top:386px;" width="152" height="66" viewBox="0 0 152 66">
    <path d="M6 26 L18 6 Q20 2 26 2 L90 2 Q96 2 100 6 L114 20 Q140 24 148 30 Q152 34 150 48 L146 52 L4 52 Q0 50 0 42 L2 30 Z" fill="var(--lime)"/>
    <path d="M22 8 L20 20 L40 20 L41 8 Z M46 8 L45 20 L82 22 L78 8 Z M84 8 L90 22 L106 22 L92 8 Z" fill="var(--white)"/>
    <circle cx="22" cy="50" r="15" fill="var(--white)"/><circle cx="22" cy="50" r="11" fill="var(--lime)"/><circle cx="22" cy="50" r="7" fill="var(--white)"/>
    <circle cx="124" cy="50" r="15" fill="var(--white)"/><circle cx="124" cy="50" r="11" fill="var(--lime)"/><circle cx="124" cy="50" r="7" fill="var(--white)"/>
  </svg>
  <div class="figure" style="left:295px; top:346px;">31</div>
  <div class="unit" style="left:293px; top:435px;">MILES DRIVING</div>

  <!-- Non-renewable energy -->
  <h2 class="section-title" style="left:653px; top:278px;">Non-Renewable Energy Use</h2>
  <svg class="icon bulb-icon" style="left:654px; top:354px;" width="90" height="128" viewBox="0 0 90 128">
    <g stroke="var(--light-blue)" stroke-width="2" stroke-linecap="round">
      <line x1="45" y1="2" x2="45" y2="12"/><line x1="18" y1="6" x2="23" y2="16"/><line x1="72" y1="6" x2="67" y2="16"/>
      <line x1="2" y1="24" x2="10" y2="29"/><line x1="88" y1="24" x2="80" y2="29"/>
    </g>
    <path d="M45 24 C20 24 12 46 16 60 C20 74 29 80 30 96 L60 96 C61 80 70 74 74 60 C78 46 70 24 45 24 Z" fill="var(--lime)"/>
    <ellipse cx="30" cy="42" rx="6" ry="9" fill="var(--white)" transform="rotate(30 30 42)"/>
    <path d="M38 68 L45 92 L52 68" fill="none" stroke="var(--olive)" stroke-width="2"/>
    <rect x="26" y="100" width="38" height="8" rx="4" fill="var(--brown)"/>
    <rect x="28" y="110" width="34" height="8" rx="4" fill="var(--olive)"/>
    <rect x="34" y="120" width="22" height="7" rx="3.5" fill="var(--brown)"/>
  </svg>
  <div class="figure" style="left:784px; top:352px;">300</div>
  <div class="unit" style="left:782px; top:439px;">HOURS OF LIGHT</div>

  <!-- Water consumption -->
  <h2 class="section-title" style="left:457px; top:540px;">Water Consumption</h2>
  <svg class="icon pool-icon" style="left:127px; top:607px;" width="126" height="120" viewBox="0 0 126 120">
    <g fill="var(--lime)">
      <path d="M24 0 L44 0 L44 8 L30 8 L30 86 L24 86 L24 6 Z"/>
      <path d="M85 0 L105 0 L105 8 L91 8 L91 86 L85 86 L85 6 Z"/>
      <rect x="30" y="30" width="55" height="8"/>
      <rect x="30" y="52" width="55" height="8"/>
    </g>
    <path d="M2 84 Q10 98 18 92 Q26 84 34 92 Q42 100 50 92 Q58 84 66 92 Q74 100 82 92 Q90 84 98 92 Q106 100 114 92 L124 84" fill="none" stroke="var(--lime)" stroke-width="7" stroke-linecap="round"/>
    <path d="M2 104 Q10 118 18 112 Q26 104 34 112 Q42 120 50 112 Q58 104 66 112 Q74 120 82 112 Q90 104 98 112 Q106 120 114 112 L124 104" fill="none" stroke="var(--lime)" stroke-width="7" stroke-linecap="round"/>
  </svg>
  <div class="figure" style="left:293px; top:607px;">XX</div>
  <div class="unit" style="left:293px; top:698px;">SWIMMING POOLS</div>

  <svg class="icon board-icon" style="left:653px; top:633px;" width="118" height="82" viewBox="0 0 118 82">
    <path d="M2 2 L82 2 L116 38 L116 80 L36 80 L2 44 Z" fill="var(--olive)"/>
    <path d="M6 6 L80 6 L110 36 L36 36 Z" fill="#fbfbf6"/>
    <path d="M40 42 L112 42 L112 54 L40 54 Z M40 60 L112 60 L112 76 L40 76 Z" fill="var(--white)"/>
    <path d="M42 50 q4 -6 8 0 t8 0 t8 0 t8 0 t8 0 t8 0 t8 0 t8 0 M42 68 q4 -6 8 0 t8 0 t8 0 t8 0 t8 0 t8 0 t8 0 t8 0" fill="none" stroke="var(--olive)" stroke-width="2"/>
    <path d="M6 14 L34 44 M6 28 L34 58 M6 42 L34 72" stroke="var(--white)" stroke-width="3"/>
  </svg>
  <p class="note" style="left:803px; top:636px;">miniscule amount of water<br>compared to corrugated paper</p>
</main>
</body>
</html>
```